Commercial Construction Company

We need a business card design based on our current logo. We are a commercial general contractor based in Southern California that specializes in bank remodels. We would like to see designs that incorporate dark blue. The final design should portray an image of professionalism and quality.

If possible, I would like to add metallic foil to the design. Thank you

```html
<!DOCTYPE html>
<html lang="en">
<head>
<meta charset="utf-8">
<title>Calder Commercial Builders – Business Card</title>
<link href="https://fonts.googleapis.com/css2?family=Montserrat:wght@600;700;800&family=Roboto:wght@400;700&display=swap" rel="stylesheet">
<style>
  :root {
    --navy: #0d4582;
    --ink: #0a0a0a;
    --paper: #f5f5f4;
    --grey: #a3a3a3;
    --stage: #e9e8e6;
    --text: #333333;
  }
  * { box-sizing: border-box; margin: 0; padding: 0; }
  html, body { width: 1200px; height: 959px; overflow: hidden; background: var(--stage); }
  .canvas { position: relative; width: 1200px; height: 959px; }
  .card {
    position: absolute; left: 260px; width: 680px; height: 389px;
    box-shadow: 0 6px 18px rgba(0,0,0,.14);
  }
  .card--back { top: 60px; background: var(--ink); }
  .card--front { top: 505px; background: var(--paper); overflow: hidden; }

  .brand { display: flex; align-items: center; gap: 12px; font-family: 'Montserrat', sans-serif; font-weight: 800; }
  .brand__dot { width: 18px; height: 18px; border-radius: 50%; background: var(--navy); flex: none; }

  .card--back .brand {
    position: absolute; left: 0; right: 0; top: 150px; justify-content: center;
    color: #ffffff; font-size: 38px; letter-spacing: .5px;
  }
  .social { position: absolute; left: 0; right: 0; top: 262px; display: flex; justify-content: center; gap: 8px; }
  .social__item { width: 18px; height: 18px; border-radius: 50%; background: var(--navy); }

  .card--front .brand {
    position: absolute; left: 40px; top: 128px; width: 250px;
    color: var(--ink); font-size: 25px; line-height: 1.15;
  }
  .divider { position: absolute; left: 318px; top: 70px; width: 2px; height: 160px; background: var(--ink); }
  .person { position: absolute; left: 346px; top: 62px; font-family: 'Montserrat', sans-serif; }
  .person__name { color: var(--navy); font-weight: 800; font-size: 23px; letter-spacing: .3px; }
  .person__role { color: var(--ink); font-weight: 700; font-size: 16px; margin-top: 2px; }
  .contacts { position: absolute; left: 346px; top: 132px; list-style: none; font-family: 'Roboto', sans-serif; font-size: 17px; color: var(--text); }
  .contacts li { display: flex; align-items: center; gap: 9px; height: 24px; }
  .contacts svg { width: 15px; height: 15px; fill: var(--navy); flex: none; }
  .address {
    position: absolute; left: 40px; top: 300px; display: flex; align-items: center; gap: 9px;
    font-family: 'Roboto', sans-serif; font-size: 18px; color: var(--text);
  }
  .address svg { width: 15px; height: 20px; fill: var(--navy); }
  .band { position: absolute; left: 0; right: 0; bottom: 0; height: 8px; display: flex; }
  .band__blue { width: 64%; background: var(--navy); }
  .band__grey { flex: 1; background: var(--grey); }
</style>
</head>
<body>
<main class="canvas">
  <section class="card card--back" aria-label="Card back">
    <div class="brand"><span class="brand__dot"></span><span>Calder Commercial</span></div>
    <div class="social" aria-label="Social links">
      <span class="social__item"></span><span class="social__item"></span><span class="social__item"></span>
    </div>
  </section>

  <section class="card card--front" aria-label="Card front">
    <div class="brand"><span class="brand__dot"></span><span>Calder Commercial</span></div>
    <div class="divider"></div>
    <div class="person">
      <p class="person__name">OWEN FAIRBANK</p>
      <p class="person__role">Director</p>
    </div>
    <ul class="contacts">
      <li><svg viewBox="0 0 16 16"><path d="M3 1l3 3-2 2c1 2 3 4 5 5l2-2 3 3-2 2C7 14 2 9 1 3z"/></svg>555.210.4410</li>
      <li><svg viewBox="0 0 16 16"><path d="M4 1h8v4H4zM1 6h14v6h-3v3H4v-3H1zM5 10v4h6v-4z"/></svg>555.210.4477</li>
      <li><svg viewBox="0 0 16 16"><path d="M1 3h14v10H1zM2 4l6 5 6-5v1L8 10 2 5z" fill-rule="evenodd"/></svg>hello@caldercb.com</li>
      <li><svg viewBox="0 0 16 16"><circle cx="8" cy="8" r="7"/><path d="M1 8h14M8 1v14" stroke="#f5f5f4" stroke-width="1.2"/></svg>www.caldercb.com</li>
    </ul>
    <p class="address"><svg viewBox="0 0 12 16"><path d="M6 0a6 6 0 0 1 6 6c0 4-6 10-6 10S0 10 0 6a6 6 0 0 1 6-6zm0 3.5a2.5 2.5 0 1 0 0 5 2.5 2.5 0 0 0 0-5z" fill-rule="evenodd"/></svg>1820 Harbor Crest Way, Suite 210 Seaview, USA</p>
    <div class="band"><span class="band__blue"></span><span class="band__grey"></span></div>
  </section>
</main>
</body>
</html>
```